Looking for a quillet ebook cover. Must meet all quillet open printing specifics. *

I need a book cover for my romance novel. The title is "Rain, Forgotten". I would like this in typographic and an illustration below ( as a reference you can see Far Shores by Doreen Plaskett). The author name is T L Venn. The story is set in England in the countryside, during fall and winter. It is a love/coming of age novel about a young couple. The girl is a writer, the boy is overcoming illness. The ending is tragic. The tone of the cover should convey an emotional read about true love and separation. It is a book for readers who enjoy novels by Bibi Trallow, Philippa Dunmore, Doreen Plaskett.

Target Market(s)

Women in their 20s and 30s who enjoy romance.

Industry/Entity Type

Publishing

Font styles to use
Sans Serif

Requirements
Must have
• You can stress the title more than the author name on the cover.
Should not have
• No photographs.

```html
<!DOCTYPE html>
<html lang="en">
<head>
<meta charset="utf-8">
<title>Rain, Forgotten — T L Venn</title>
<link rel="stylesheet" href="https://fonts.googleapis.com/css2?family=Crimson+Text:wght@400;600&display=swap">
<style>
  :root {
    --coral: #f48a7c;
    --coral-light: #f89d90;
    --coral-deep: #ee7d6f;
    --title-light: #fff6f2;
    --title-dark: #141010;
    --figure-warm: #e9a13a;
    --figure-red: #d8322a;
    --snow: #fdf3ee;
  }
  html, body {
    margin: 0;
    padding: 0;
    width: 800px;
    height: 1200px;
    overflow: hidden;
    background: var(--coral);
  }
  .cover {
    position: relative;
    width: 800px;
    height: 1200px;
    overflow: hidden;
    background:
      radial-gradient(ellipse at 30% 8%, var(--coral-light) 0%, transparent 55%),
      radial-gradient(ellipse at 80% 85%, var(--coral-deep) 0%, transparent 60%),
      var(--coral);
    font-family: "Crimson Text", Georgia, serif;
    text-align: center;
  }
  .snowfall {
    position: absolute;
    inset: 0;
    width: 800px;
    height: 1200px;
  }
  .title {
    position: absolute;
    top: 150px;
    left: 0;
    width: 800px;
    margin: 0;
    font-weight: 400;
    line-height: 1;
  }
  .title-first {
    display: block;
    color: var(--title-light);
    font-size: 108px;
    letter-spacing: 1px;
    margin-left: -30px;
  }
  .title-second {
    display: block;
    color: var(--title-dark);
    font-size: 124px;
    margin-top: -14px;
  }
  .illustration {
    position: absolute;
    left: 250px;
    top: 545px;
    width: 330px;
    height: 280px;
    border-radius: 50%;
    background:
      radial-gradient(ellipse at 50% 40%, var(--figure-red) 0%, var(--figure-warm) 28%, rgba(233,161,58,0.6) 40%, transparent 55%),
      radial-gradient(ellipse at 50% 75%, var(--snow) 0%, rgba(253,243,238,0.6) 35%, transparent 65%);
  }
  .author {
    position: absolute;
    top: 1020px;
    left: 0;
    width: 800px;
    margin: 0;
    color: var(--title-light);
    font-size: 118px;
    font-weight: 400;
    line-height: 1;
    letter-spacing: 2px;
  }
</style>
</head>
<body>
  <main class="cover">
    <svg class="snowfall" viewBox="0 0 800 1200" aria-hidden="true">
      <g fill="#ffffff" opacity="0.7">
        <circle cx="120" cy="60" r="2"/><circle cx="240" cy="110" r="1.5"/>
        <circle cx="380" cy="40" r="2"/><circle cx="520" cy="90" r="1.5"/>
        <circle cx="660" cy="50" r="2"/><circle cx="720" cy="140" r="1.5"/>
        <circle cx="60" cy="180" r="1.5"/><circle cx="300" cy="220" r="2"/>
        <circle cx="590" cy="260" r="1.5"/><circle cx="700" cy="320" r="2"/>
        <circle cx="90" cy="400" r="2"/><circle cx="200" cy="480" r="1.5"/>
        <circle cx="640" cy="470" r="2"/><circle cx="730" cy="560" r="1.5"/>
        <circle cx="150" cy="620" r="2"/><circle cx="680" cy="680" r="1.5"/>
        <circle cx="80" cy="760" r="1.5"/><circle cx="720" cy="800" r="2"/>
        <circle cx="230" cy="880" r="1.5"/><circle cx="600" cy="920" r="2"/>
        <circle cx="400" cy="480" r="1.5"/><circle cx="460" cy="20" r="1.5"/>
      </g>
    </svg>

    <h1 class="title">
      <span class="title-first">RAIN,</span>
      <span class="title-second">Forgotten</span>
    </h1>

    <div class="illustration" role="img" aria-label="Illustration of a small figure in a red beret and yellow scarf sitting huddled on a patch of snow"></div>

    <p class="author">T L VENN</p>
  </main>
</body>
</html>
```